Design Banner for Insurance agency ( Publisher format )

I am looking to design banner for auto insurance agency. With the following wording listed below. I would like creative ideas. We have a great location with a lot of foot traffic.

Banner -1( Size 8 by 2.5 Feet )
Logo
Name : Granite Peak Insurance agency
Insert some logos for insurance companies, Corvelle, tallmark, Brenwick, Quilo
Insert the following sentence :
I’m not perfect, just insured.
Instant Insurance Start @ $29 Mo

Banner -2 ( 8 by 2.5 Feet)
Logo- Name
I have good brakes, do u have good insurance?
FAST SR-22

Need color matching logo color.
( Make arrow on the side of the banners- I will hang it next door to my office)

```html
<!DOCTYPE html>
<html lang="en">
<head>
<meta charset="utf-8">
<title>Granite Peak Insurance Agency Banner</title>
<link rel="stylesheet" href="https://fonts.googleapis.com/css2?family=Montserrat:wght@600;700;800&family=Italianno&family=Ubuntu:wght@400;500&display=swap">
<style>
  :root {
    --forest: #0c2310;
    --white: #ffffff;
    --gold: #a89a55;
    --gold-box: #b3a465;
    --olive: #6a6428;
    --ink: #11240f;
    --arrow-light: #ece6e2;
    --arrow-dark: #7d6f6a;
    --partner-blue: #2a63c8;
    --partner-red: #c8322b;
  }
  * { margin: 0; padding: 0; box-sizing: border-box; }
  html, body { width: 1200px; height: 375px; overflow: hidden; background: var(--forest); }
  .banner {
    position: relative;
    width: 1200px;
    height: 375px;
    background: var(--forest);
    font-family: "Montserrat", Arial, sans-serif;
  }
  .arrow { position: absolute; top: 84px; }
  .arrow--left { left: 20px; }
  .arrow--right { left: 971px; }

  .agency-name {
    position: absolute;
    left: 375px;
    top: 54px;
    white-space: nowrap;
    line-height: 1;
  }
  .agency-name__lead {
    color: var(--white);
    font-weight: 800;
    font-size: 43px;
    letter-spacing: -0.5px;
  }
  .agency-name__rest {
    color: var(--gold);
    font-weight: 700;
    font-size: 33px;
    margin-left: 8px;
  }
  .name-rule {
    position: absolute;
    left: 407px;
    top: 110px;
    width: 362px;
    height: 2px;
    background: var(--gold);
  }
  .agency-suffix {
    position: absolute;
    left: 780px;
    top: 101px;
    color: var(--white);
    font-weight: 600;
    font-size: 19px;
    letter-spacing: 1px;
    line-height: 1;
  }
  .tagline {
    position: absolute;
    left: 0;
    width: 1200px;
    top: 116px;
    text-align: center;
    font-family: "Italianno", cursive;
    font-size: 88px;
    color: var(--olive);
    line-height: 1;
  }
  .offer {
    position: absolute;
    left: 311px;
    top: 213px;
    display: flex;
    height: 50px;
  }
  .offer__title {
    background: var(--white);
    color: var(--ink);
    font-family: "Ubuntu", Arial, sans-serif;
    font-size: 48px;
    font-weight: 400;
    width: 392px;
    display: flex;
    align-items: center;
    padding-left: 5px;
    white-space: nowrap;
  }
  .offer__price {
    background: var(--gold-box);
    color: var(--ink);
    font-family: "Ubuntu", Arial, sans-serif;
    font-weight: 500;
    font-size: 25px;
    width: 205px;
    display: flex;
    align-items: center;
    justify-content: center;
    white-space: nowrap;
  }
  .partner-mark { position: absolute; display: block; }
  .partner-name {
    position: absolute;
    font-family: "Montserrat", Arial, sans-serif;
    font-weight: 700;
    line-height: 1;
    white-space: nowrap;
  }
  .partner-mark--corvelle { left: 69px; top: 220px; width: 70px; height: 90px; background: var(--partner-blue); }
  .partner-name--corvelle { left: 19px; top: 317px; color: var(--white); font-size: 34px; }
  .partner-mark--quilo { left: 224px; top: 310px; width: 36px; height: 36px; border-radius: 50%; background: var(--white); }
  .partner-name--quilo { left: 268px; top: 312px; color: var(--white); font-size: 34px; }
  .partner-name--tallmark { left: 827px; top: 313px; color: var(--partner-blue); font-size: 37px; }
  .partner-mark--brenwick { left: 1113px; top: 227px; width: 67px; height: 88px; background: var(--partner-red); }
  .partner-name--brenwick { left: 1063px; top: 324px; color: var(--partner-red); font-size: 25px; }
</style>
</head>
<body>
<main class="banner">
  <svg class="arrow arrow--left" width="189" height="77" viewBox="0 0 189 77" aria-hidden="true">
    <defs>
      <linearGradient id="arrow-shade-left" x1="0" x2="1">
        <stop offset="0" stop-color="var(--arrow-light)"/>
        <stop offset="0.6" stop-color="#d9d0cb"/>
        <stop offset="1" stop-color="var(--arrow-dark)"/>
      </linearGradient>
    </defs>
    <polygon points="0,19 100,19 100,0 189,38.5 100,77 100,58 0,58" fill="url(#arrow-shade-left)"/>
  </svg>

  <div class="agency-name">
    <span class="agency-name__lead">Granite</span><span class="agency-name__rest">Peak Insurance</span>
  </div>
  <div class="name-rule"></div>
  <span class="agency-suffix">Agency</span>

  <p class="tagline">I'm not perfect, just insured</p>

  <div class="offer">
    <span class="offer__title">Instant Insurance</span>
    <span class="offer__price">Start @ $29 Mo</span>
  </div>

  <svg class="arrow arrow--right" width="189" height="77" viewBox="0 0 189 77" aria-hidden="true">
    <defs>
      <linearGradient id="arrow-shade-right" x1="0" x2="1">
        <stop offset="0" stop-color="var(--arrow-light)"/>
        <stop offset="0.65" stop-color="#d9d0cb"/>
        <stop offset="1" stop-color="var(--arrow-dark)"/>
      </linearGradient>
    </defs>
    <polygon points="0,19 100,19 100,0 189,38.5 100,77 100,58 0,58" fill="url(#arrow-shade-right)"/>
  </svg>

  <span class="partner-mark partner-mark--corvelle"></span>
  <span class="partner-name partner-name--corvelle">Corvelle</span>
  <span class="partner-mark partner-mark--quilo"></span>
  <span class="partner-name partner-name--quilo">Quilo</span>
  <span class="partner-name partner-name--tallmark">Tallmark</span>
  <span class="partner-mark partner-mark--brenwick"></span>
  <span class="partner-name partner-name--brenwick">Brenwick</span>
</main>
</body>
</html>
```